Industrial Professional Business Card Design (Vantrel Systems)

Would like professional looking business cards. Not too busy leaning towards minimal. Should have a slogan like:
"Industrial Automation and Control".

We are a tech company that programs industrial PLC computers. We also develop custom hardware solutions. Please use the logo for inspiration.

Target Market(s)

Mining, industrial, processing, automation, factory

Industry/Entity Type

Engineering

Contact Information for Business Card

Name, phone, email, website. job title.

Font styles to use
Other font styles liked:
• droid sans

Requirements
Must have
• Use colours that go well with the logo. Not too busy design.

```html
<!DOCTYPE html>
<html lang="en">
<head>
<meta charset="utf-8">
<title>Vantrel Systems – Business Card</title>
<link href="https://fonts.googleapis.com/css2?family=Noto+Sans:wght@400;700&display=swap" rel="stylesheet">
<style>
  :root {
    --bg: #2b2b2d;
    --card: #ffffff;
    --navy: #1f2557;
    --blue: #1f5f8f;
    --orange: #f26a21;
    --wash: #e9e9ee;
  }
  * { box-sizing: border-box; margin: 0; padding: 0; }
  html, body { width: 1200px; height: 900px; overflow: hidden; }
  body {
    background: var(--bg);
    font-family: "Noto Sans", sans-serif;
    position: relative;
  }
  .card {
    position: absolute;
    left: 260px;
    width: 680px;
    height: 388px;
    background: var(--card);
    border-radius: 22px;
    overflow: hidden;
  }
  .card--front { top: 42px; }
  .card--back { top: 470px; }

  .card__wash {
    position: absolute;
    right: -120px;
    top: -140px;
    width: 460px;
    height: 460px;
    border-radius: 50%;
    background: radial-gradient(circle, var(--wash) 0%, rgba(233,233,238,0.6) 55%, rgba(255,255,255,0) 72%);
  }

  /* Front */
  .brand {
    position: absolute;
    left: 0; right: 0;
    top: 140px;
    text-align: center;
  }
  .brand__row {
    display: inline-flex;
    align-items: center;
    gap: 16px;
  }
  .brand__dot {
    width: 34px; height: 34px;
    border-radius: 50%;
    background: var(--orange);
  }
  .brand__name {
    font-size: 46px;
    font-weight: 700;
    color: var(--navy);
    letter-spacing: 0.5px;
  }
  .brand__tagline {
    margin-top: 6px;
    font-size: 17px;
    color: var(--blue);
    letter-spacing: 1.5px;
  }

  /* Back */
  .ident {
    position: absolute;
    left: 70px;
    top: 100px;
    width: 230px;
    height: 130px;
    display: flex;
    align-items: center;
    gap: 12px;
  }
  .ident__dot {
    width: 26px; height: 26px;
    border-radius: 50%;
    background: var(--orange);
    flex: none;
  }
  .ident__name {
    font-size: 27px;
    font-weight: 700;
    color: var(--navy);
    line-height: 1.1;
  }
  .divider {
    position: absolute;
    left: 318px;
    top: 96px;
    width: 2px;
    height: 140px;
    background: var(--navy);
  }
  .contact {
    position: absolute;
    left: 342px;
    top: 96px;
  }
  .contact__name {
    font-size: 27px;
    font-weight: 700;
    color: var(--navy);
    line-height: 1.1;
  }
  .contact__title {
    font-size: 15px;
    color: var(--orange);
    margin-bottom: 12px;
  }
  .contact__list { list-style: none; }
  .contact__item {
    display: flex;
    align-items: center;
    gap: 10px;
    font-size: 15px;
    color: var(--navy);
    line-height: 26px;
  }
  .contact__icon { width: 15px; height: 15px; flex: none; }

  .slogan {
    position: absolute;
    left: 0; right: 0;
    bottom: 46px;
    height: 30px;
  }
  .slogan__line {
    position: absolute;
    top: 50%;
    height: 2px;
    background: var(--orange);
  }
  .slogan__line--left { left: 0; width: 158px; }
  .slogan__line--right { right: 0; width: 150px; }
  .slogan__line--left::after,
  .slogan__line--right::before {
    content: "";
    position: absolute;
    top: -4px;
    width: 10px; height: 10px;
    border-radius: 50%;
    background: var(--orange);
  }
  .slogan__line--left::after { right: -5px; }
  .slogan__line--right::before { left: -5px; }
  .slogan__text {
    position: absolute;
    left: 0; right: 0;
    text-align: center;
    font-size: 20px;
    color: var(--navy);
    letter-spacing: 1px;
    line-height: 30px;
  }
</style>
</head>
<body>

  <section class="card card--front">
    <div class="card__wash" aria-hidden="true"></div>
    <div class="brand">
      <div class="brand__row">
        <span class="brand__dot"></span>
        <span class="brand__name">Vantrel Systems</span>
      </div>
      <p class="brand__tagline">Industrial Automation and Control</p>
    </div>
  </section>

  <section class="card card--back">
    <div class="card__wash" aria-hidden="true"></div>

    <div class="ident">
      <span class="ident__dot"></span>
      <span class="ident__name">Vantrel<br>Systems</span>
    </div>

    <div class="divider"></div>

    <div class="contact">
      <p class="contact__name">Daniel Reyes</p>
      <p class="contact__title">Managing Director</p>
      <ul class="contact__list">
        <li class="contact__item">
          <svg class="contact__icon" viewBox="0 0 16 16"><path fill="#f26a21" d="M3.5 1.5l2.5 3-1.5 1.7c.8 1.8 2.2 3.2 4 4l1.7-1.5 3 2.5-1.5 2.5C7 13.5 2.5 9 1.5 3z"/></svg>
          (03) 9555 0142
        </li>
        <li class="contact__item">
          <svg class="contact__icon" viewBox="0 0 16 16"><rect x="1" y="3" width="14" height="10" fill="#f26a21"/><path d="M1 3l7 6 7-6" fill="none" stroke="#fff" stroke-width="1.3"/></svg>
          daniel@vantrelsystems.com
        </li>
        <li class="contact__item">
          <svg class="contact__icon" viewBox="0 0 16 16" fill="none" stroke="#f26a21" stroke-width="1.3"><circle cx="8" cy="8" r="6.5"/><ellipse cx="8" cy="8" rx="3" ry="6.5"/><path d="M1.5 8h13M2.5 5h11M2.5 11h11"/></svg>
          www.vantrelsystems.com
        </li>
      </ul>
    </div>

    <div class="slogan">
      <span class="slogan__line slogan__line--left"></span>
      <p class="slogan__text">Industrial Automation and Control</p>
      <span class="slogan__line slogan__line--right"></span>
    </div>
  </section>

</body>
</html>
```